Romparoo - launching a new children's entertainment venue

Create a flyer (to be used online and offline) to promote a new business

Business name (tbc). Current considerations are:
# "Skylark for KIDS"
# "SK for KIDS"
# "SK Parties"

Concept
# A creative play space for young children
# To be used for either (i) birthday parties or (ii) general play area available for Mums/parents groups to hire

Facilities:
# General play space
# Basketball, soccer
# Ball pit
# Video games
# Movies

Room designed for 2-8 year olds in mind

Catering available:
# Party pies, sausage rolls and mini franks
# Potato chips
# Cordial and water
Note - cake not included
Kitchen facility available.

Party host

Use of parents retreat room

Packages (costs):
# 2 hour party with catering pack and host $220 (up to 10 children, $17.50 per child for additional children)
# 2 hour party - BYO and host $200 (up to 10 children, $15 per child for additional children)
# Casual hire (exclusive use of room and parents retreat) - $50 per hour

Note - we also require a new logo for this new business concept

Existing business is called Skylark Sports, a basketball training and development facility. The new business needs to be linked to Skylark Sports from a banding perspective although does require its own identity

Brand essence - fun, vibrant, colourful, engaging

Target Market(s)

Mums of children aged 2-8 years

Industry/Entity Type

Entertainment

Logo Text

Name "Skylark for KIDS" (although name is not 100% confirmed)

Font styles to use
Serif
Sans Serif

Requirements
Must have
• Must be vibrant, colourful and fun
• Get across sense of energy
Nice to have
• Some sort of link to existing business "Skylark Sports" logos are attached
• Although we have an open mind to a totally seperate brand

```html
<!DOCTYPE html>
<html lang="en">
<head>
<meta charset="utf-8">
<title>Skylark Sports – Party Flyer</title>
<link rel="stylesheet" href="https://fonts.googleapis.com/css2?family=Oswald:wght@500;600&family=Signika:wght@600&family=Poppins:wght@500&family=Roboto+Condensed:wght@500&display=swap">
<style>
  :root{
    --page:#e4e4e4;
    --black:#0b0b0b;
    --blue:#169fdc;
    --yellow:#f4e800;
    --green:#2faa2a;
    --white:#ffffff;
    --ink:#1a1a1a;
    --price:#1aa0e0;
    --bullet:#c9e03a;
  }
  *{box-sizing:border-box;margin:0;padding:0}
  html,body{width:1200px;height:1200px;overflow:hidden;background:var(--page)}
  .flyer{position:absolute;left:200px;top:35px;width:800px;height:1130px;overflow:hidden;background:var(--blue);box-shadow:0 10px 30px rgba(0,0,0,.25)}
  .flyer-bg{position:absolute;inset:0}
  .photo{position:absolute;border-radius:50%;overflow:hidden}
  .photo-hero{left:400px;top:-130px;width:530px;height:530px;border:10px solid var(--green);border-bottom-color:var(--yellow);background:radial-gradient(circle at 45% 40%,#f2c6a8 0,#e8a07e 18%,#d8262a 40%,#c5141b 62%,#f0d640 85%)}
  .photo-family{left:300px;top:235px;width:190px;height:190px;border:8px solid var(--white);background:radial-gradient(circle at 50% 45%,#f3d3bd 0,#e7c29a 30%,#a8c9e8 60%,#f0e3c0 100%);box-shadow:0 4px 10px rgba(0,0,0,.3)}
  .photo-lounge{left:545px;top:565px;width:200px;height:200px;border:9px solid var(--yellow);background:linear-gradient(135deg,#e0303a 0,#d92a36 45%,#5a4b9b 55%,#3a2f2a 90%)}
  .photo-hall{left:475px;top:775px;width:160px;height:160px;border:8px solid var(--yellow);background:linear-gradient(180deg,#d9d4cc 0,#8a8580 45%,#2f8a36 65%,#1f6f28 100%)}
  .photo-cinema{left:640px;top:760px;width:150px;height:150px;border:8px solid var(--yellow);background:linear-gradient(180deg,#1c1c1c 0,#3a2a22 45%,#2c8a34 62%,#1d4aa0 100%)}
  .brand{position:absolute;left:90px;top:60px;width:250px;text-align:center}
  .brand-dot{width:130px;height:130px;border-radius:50%;background:#c9631f;margin:0 auto 18px}
  .brand-name{font-family:'Oswald',sans-serif;font-weight:600;color:var(--white);font-size:38px;line-height:1.05;letter-spacing:1px}
  .headline{position:absolute;left:60px;top:445px;font-family:'Oswald',sans-serif;font-weight:600;line-height:1.05;text-transform:uppercase;white-space:nowrap}
  .headline-top{color:var(--yellow);font-size:54px}
  .headline-bottom{color:var(--white);font-size:50px}
  .label{position:absolute;left:0;height:44px;padding:0 30px 0 50px;display:flex;align-items:center;background:var(--yellow);border-radius:0 22px 22px 0;font-family:'Poppins',sans-serif;font-weight:500;font-size:19px;color:var(--ink);white-space:nowrap;box-shadow:0 3px 6px rgba(0,0,0,.2)}
  .label-facilities{top:578px;width:200px}
  .label-catering{top:738px;width:310px}
  .list{position:absolute;list-style:none;font-family:'Signika',sans-serif;font-weight:600;color:var(--white);font-size:19px;line-height:30px;white-space:nowrap}
  .list li{position:relative;padding-left:22px}
  .list li::before{content:"";position:absolute;left:0;top:12px;width:7px;height:7px;border-radius:50%;background:var(--bullet)}
  .list li.plain::before{display:none}
  .facilities-a{left:70px;top:632px}
  .facilities-b{left:300px;top:632px}
  .catering{left:80px;top:792px}
  .packages{position:absolute;list-style:none;font-family:'Roboto Condensed',sans-serif;font-weight:500;color:var(--ink);font-size:14.5px;line-height:18px}
  .packages li{position:relative;padding-left:24px;margin-bottom:16px}
  .packages li::before{content:"";position:absolute;left:0;top:6px;width:9px;height:9px;border-radius:50%;background:var(--price)}
  .packages .cost{color:var(--price)}
  .packages-main{left:55px;top:1020px;width:430px}
  .packages-side{left:510px;top:1005px;width:260px;font-size:13px;line-height:16px}
</style>
</head>
<body>
<main class="flyer">
  <svg class="flyer-bg" viewBox="0 0 800 1130" width="800" height="1130" aria-hidden="true">
    <path d="M0 0H800V330C560 330 260 330 0 440Z" fill="var(--yellow)"/>
    <path d="M0 0H800V300C560 310 260 320 0 420Z" fill="var(--green)"/>
    <path d="M0 0H800V290C560 300 260 305 0 405Z" fill="var(--black)"/>
    <path d="M0 970C250 925 520 945 800 900V1130H0Z" fill="var(--yellow)"/>
    <path d="M0 995C250 948 520 965 800 922V1130H0Z" fill="var(--white)"/>
  </svg>

  <div class="photo photo-hero" role="img" aria-label="Photo: excited boy in party hat holding a red gift, friends behind"></div>
  <div class="photo photo-family" role="img" aria-label="Photo: mother and young children playing together"></div>
  <div class="photo photo-lounge" role="img" aria-label="Photo: parents retreat room with red and purple walls and armchairs"></div>
  <div class="photo photo-hall" role="img" aria-label="Photo: play hall with green turf and bench table"></div>
  <div class="photo photo-cinema" role="img" aria-label="Photo: movie corner with blue benches on turf"></div>

  <div class="brand">
    <div class="brand-dot"></div>
    <div class="brand-name">SKYLARK<br>SPORTS</div>
  </div>

  <h1 class="headline">
    <span class="headline-top">Fun, Vibrant</span><br>
    <span class="headline-bottom">Colourful, Engaging</span>
  </h1>

  <div class="label label-facilities">FACILITIES:</div>
  <ul class="list facilities-a">
    <li>General play space</li>
    <li>Basketball, soccer</li>
    <li>Ball pit</li>
  </ul>
  <ul class="list facilities-b">
    <li>Video games</li>
    <li>Movies</li>
  </ul>

  <div class="label label-catering">CATERING AVAILABLE:</div>
  <ul class="list catering">
    <li>Party pies, sausage rolls and mini franks</li>
    <li class="plain"># Potato chips</li>
    <li># Cordial and water</li>
    <li class="plain">Note - cake not included</li>
    <li>Kitchen facility available.</li>
  </ul>

  <ul class="packages packages-main">
    <li>2 hour party with catering pack and host <span class="cost">$220</span><br>(up to 10 children, <span class="cost">$17.50</span> per child for additional children)</li>
    <li>2 hour party - BYO and host <span class="cost">$200</span> (up to 10 children,<br><span class="cost">$15</span> per child for additional children)</li>
  </ul>
  <ul class="packages packages-side">
    <li>Casual hire<br>(exclusive use of room and parents retreat)<br><span class="cost">$50</span> per hour</li>
  </ul>
</main>
</body>
</html>
```